Special offers flyer for IT firm

We need a flyer design for our IT technical services firm based in Melbourne, Australia. We want to advertise two offerings on a double sided flyer.
-
First Offering:
Free computer system health report and audit
- health check of servers, workstations and network
- comprehensive non-technical report including recommendations
-
Second Offering:
Discounted technical support - $80* per hour
- day to day helpdesk support
- system upgrades and migrations
- cloud services design, implementation and support
- web hosting, domain names and email filtering

*exclusive of GST (must denote somewhere in small print)
-
The contact details for the offer must include room for Phone, Email and Web Address.

I am not set on the text, or any particular format, additional images would be good to break up the pages.

Target Market(s)

Professional Services small business owners (under 30 staff)

Industry/Entity Type

Computer

Requirements
Must have
• DL Sized document (210mmx99mm) portrait or landscape, double sided.

```html
<!DOCTYPE html>
<html lang="en">
<head>
<meta charset="utf-8">
<title>Special Offers Flyer – NorthGrid IT</title>
<link rel="stylesheet" href="https://fonts.googleapis.com/css2?family=Mulish:wght@600;700;800;900&display=swap">
<style>
  :root {
    --brand-blue: #1e66d0;
    --ink: #111111;
    --paper: #ffffff;
    --page: #ffffff;
    --muted: #dfe8f7;
    --shadow: rgba(0,0,0,0.28);
  }
  * { margin: 0; padding: 0; box-sizing: border-box; }
  html, body { width: 900px; height: 1200px; overflow: hidden; background: var(--page); }
  body { position: relative; font-family: "Mulish", Arial, sans-serif; color: var(--ink); }

  .flyer-side {
    position: absolute; left: 41px; width: 818px; height: 386px;
    background: var(--paper); box-shadow: 2px 3px 6px var(--shadow); overflow: hidden;
  }
  .side-front { top: 144px; }
  .side-back { top: 569px; }

  /* Front */
  .offer-ticker {
    position: absolute; top: 0; left: 0; width: 100%; height: 69px;
    background: var(--brand-blue); overflow: hidden;
  }
  .offer-ticker-text {
    position: absolute; top: 25px; left: -180px; white-space: nowrap;
    color: var(--paper); font-weight: 800; font-size: 31px; letter-spacing: 0.3px;
    word-spacing: 2px; text-shadow: 1px 2px 3px rgba(0,0,0,0.35);
  }
  .offer-ticker-text span { margin-right: 17px; }
  .hero-photo {
    position: absolute; top: 72px; left: 0; width: 100%; height: 191px;
    background:
      radial-gradient(ellipse 260px 110px at 260px 70px, #d79a7c 0%, #b97256 45%, rgba(60,40,35,0) 75%),
      linear-gradient(160deg, #6b6b6b 0%, #2a2a2a 35%, #111 60%, #3a3a3a 100%);
  }
  .free-headline {
    position: absolute; left: 36px; top: 185px; color: var(--paper);
    font-weight: 900; font-size: 86px; line-height: 1; letter-spacing: -2px;
    height: 78px; overflow: hidden;
  }
  .offer-list { position: absolute; left: 38px; top: 284px; list-style: none; }
  .offer-list li { font-weight: 700; font-size: 16.5px; line-height: 27.5px; }

  .brand-mark {
    position: absolute; display: flex; align-items: center; gap: 10px;
    font-weight: 700; font-size: 34px; color: var(--ink); letter-spacing: 0.5px;
  }
  .brand-mark .brand-dot { width: 16px; height: 16px; background: var(--brand-blue); border-radius: 50%; }
  .side-front .brand-mark { left: 580px; top: 295px; }
  .side-back .brand-mark { left: 580px; top: 296px; }

  /* Back */
  .service-panel {
    position: absolute; top: 0; left: 0; width: 100%; height: 259px; background: var(--brand-blue);
  }
  .support-photo {
    position: absolute; left: 0; top: 38px; width: 409px; height: 186px;
    border: 3px solid var(--paper); border-left: 0;
    background:
      linear-gradient(90deg, #f1ece8 0%, #e8d2c6 16%, #f4f4f4 17%, #f4f4f4 33%, rgba(255,255,255,0) 33.5%),
      linear-gradient(180deg, #eef1f3 0%, #9aa3aa 45%, #2b2f33 70%, #d9dcdf 100%);
  }
  .service-title {
    position: absolute; left: 430px; top: 34px; color: var(--paper);
    font-weight: 800; font-size: 32px; letter-spacing: 0.5px;
    text-shadow: 1px 2px 3px rgba(0,0,0,0.3);
  }
  .service-list {
    position: absolute; left: 430px; top: 88px; list-style: none; color: var(--paper);
    font-weight: 700; font-size: 13.6px;
  }
  .service-list li { line-height: 17px; margin-bottom: 9px; }
  .tax-note {
    position: absolute; left: 665px; top: 236px; color: var(--muted);
    font-size: 9px; font-weight: 600;
  }
  .contact-block { position: absolute; left: 31px; top: 288px; }
  .contact-heading { color: var(--brand-blue); font-weight: 700; font-size: 24px; margin-bottom: 8px; }
  .contact-line { font-weight: 700; font-size: 13px; line-height: 18px; white-space: pre; }
</style>
</head>
<body>
  <section class="flyer-side side-front">
    <div class="offer-ticker">
      <div class="offer-ticker-text"><span>SPECIAL OFFERS</span><span>SPECIAL OFFERS</span><span>SPECIAL OFFERS</span><span>SPECIAL OFFERS</span></div>
    </div>
    <div class="hero-photo" role="img" aria-label="Close-up photo of a hand typing on a dark computer keyboard"></div>
    <div class="free-headline">FREE</div>
    <ul class="offer-list">
      <li>Computer system health report and audit</li>
      <li>Health check of servers, workstations and network</li>
      <li>Comprehensive non-technical report including recommendations</li>
    </ul>
    <div class="brand-mark"><span class="brand-dot"></span>NorthGrid IT</div>
  </section>

  <section class="flyer-side side-back">
    <div class="service-panel">
      <div class="support-photo" role="img" aria-label="Photo of a helpdesk operator with headset beside office computer workstations"></div>
      <h2 class="service-title">ALSO AVAILABLE</h2>
      <ul class="service-list">
        <li>Discounted technical support - $80* per hour</li>
        <li>Day to day helpdesk support</li>
        <li>System upgrades and migrations</li>
        <li>Cloud services design, implementation<br>and support</li>
        <li>Web hosting, domain names and email filtering</li>
      </ul>
      <p class="tax-note">*exclusive of GST</p>
    </div>
    <div class="contact-block">
      <h3 class="contact-heading">Call or Email NOW</h3>
      <p class="contact-line">P: &lt;Insert Phone Number&gt;  E: &lt;Insert Email Address&gt;</p>
      <p class="contact-line">www.northgridit.com.au</p>
    </div>
    <div class="brand-mark"><span class="brand-dot"></span>NorthGrid IT</div>
  </section>
</body>
</html>
```